Business card design needed

We are a manufacturing business based in Archerfield, Brisbane, Queensland. We Insulate airconditioning ductwork and also manufacture some duct.
Updates

Hi guys, thanks for all the responses, they are looking really great

I have attached a couple of better quality photos of the products we use or manufacture, they don't "need" to be used in the card but i thought it was worth uploading them

I will be picking the final card in the next couple of days

Thanks for the response.

I think this will be the last update but i have included what we do so it can be added to the back of a card.

Target Market(s)

Local contractors

Industry/Entity Type

Business

Contact Information for Business Card

Corvane Insulation
Mark Delaney
87 Tilbury Road
Marlow Creek, QLD, 4110
mark@corvaneinsulation.com.au
Phone: 07 3519 6042

Requirements
Must have
• our logo which i have attached

Also, on the back of the card it would be nice to have what we do

-Duct lagging (internal and external)
-Manufacture of P3 boxes
-Supply of glasswool, foam insulation, ductboard, foils, tapes & pins.

```html
<!DOCTYPE html>
<html lang="en">
<head>
<meta charset="utf-8">
<title>Corvane Insulation – Business Cards</title>
<link rel="stylesheet" href="https://fonts.googleapis.com/css2?family=Exo+2:wght@400;500;700&family=Open+Sans:wght@400;500&display=swap">
<style>
  :root {
    --backdrop: #6e3b22;
    --card-white: #ffffff;
    --ink-dark: #3b3b3d;
    --band-dark: #2f2f31;
    --band-light: #7a7b7e;
    --orange-deep: #e85a26;
    --orange-bright: #f18b25;
    --white: #ffffff;
    --text-font: "Exo 2", sans-serif;
    --url-font: "Open Sans", sans-serif;
  }
  * { box-sizing: border-box; margin: 0; padding: 0; }
  html, body { width: 1200px; height: 783px; overflow: hidden; }
  body { background: var(--backdrop); position: relative; font-family: var(--text-font); }

  .card {
    position: absolute;
    width: 504px;
    height: 288px;
    background: var(--card-white);
    box-shadow: 0 3px 8px rgba(0,0,0,0.35);
    overflow: hidden;
  }
  .card--front   { left: 72px;  top: 72px; }
  .card--back    { left: 624px; top: 74px; }
  .card--pattern { left: 67px;  top: 429px; }
  .card--orange  { left: 624px; top: 429px;
    background: linear-gradient(180deg, var(--orange-deep), var(--orange-bright)); }

  .wordmark {
    position: absolute;
    left: 0; right: 0;
    display: flex;
    align-items: center;
    justify-content: center;
    gap: 14px;
    font-family: var(--text-font);
    font-weight: 700;
    color: var(--ink-dark);
    letter-spacing: 1px;
    white-space: nowrap;
  }
  .wordmark__square {
    width: 28px; height: 28px;
    background: var(--orange-deep);
    flex: none;
  }
  .card--front .wordmark   { top: 54px; font-size: 28px; }
  .card--back .wordmark    { top: 100px; font-size: 34px; }
  .card--back .wordmark__square { width: 34px; height: 34px; }
  .card--pattern .wordmark { top: 104px; font-size: 34px; }
  .card--orange .wordmark  { top: 100px; font-size: 34px; color: var(--white); }

  .website {
    position: absolute;
    left: 0; right: 0;
    text-align: center;
    font-family: var(--url-font);
    font-size: 19px;
    letter-spacing: 3px;
    color: var(--ink-dark);
    white-space: nowrap;
  }
  .card--back .website    { top: 250px; }
  .card--pattern .website { top: 246px; }
  .card--orange .website  { top: 246px; color: var(--white); }

  .name-band {
    position: absolute;
    left: 0; top: 155px;
    width: 100%; height: 39px;
    background: linear-gradient(90deg, var(--band-dark), var(--band-light));
    color: var(--white);
    font-size: 19px;
    font-weight: 500;
    letter-spacing: 2px;
    text-align: center;
    line-height: 39px;
  }
  .contact-panel {
    position: absolute;
    left: 0; top: 199px;
    width: 100%; height: 89px;
    background: linear-gradient(90deg, var(--orange-deep), var(--orange-bright));
    color: var(--white);
    font-size: 14px;
    letter-spacing: 0.6px;
    text-align: center;
    padding-top: 9px;
    white-space: nowrap;
  }
  .contact-panel__row {
    display: flex;
    justify-content: center;
    align-items: center;
    gap: 12px;
    height: 25px;
  }
  .contact-item { display: inline-flex; align-items: center; gap: 5px; }
  .contact-item svg { width: 11px; height: 11px; fill: var(--white); }
  .contact-panel__address { margin-top: 4px; letter-spacing: 1.2px; }
</style>
</head>
<body>

  <section class="card card--front" aria-label="Business card front">
    <div class="wordmark"><span class="wordmark__square"></span>Corvane Insulation</div>
    <div class="name-band">Mark Delaney</div>
    <div class="contact-panel">
      <div class="contact-panel__row">
        <span class="contact-item">
          <svg viewBox="0 0 12 12" aria-hidden="true"><path d="M3 1l2 2.5-1.2 1.2a6 6 0 0 0 3.5 3.5L8.5 7 11 9l-1.5 2C5 11 1 7 1 2.5z"/></svg>
          07 3519 6042
        </span>
        <span class="contact-item">
          <svg viewBox="0 0 12 12" aria-hidden="true"><path d="M1 3h10v7H1z M1 3l5 4 5-4" fill="none" stroke="#fff" stroke-width="1.4"/></svg>
          mark@corvaneinsulation.com.au
        </span>
      </div>
      <div class="contact-panel__row">
        <span class="contact-item">
          <svg viewBox="0 0 12 12" aria-hidden="true"><circle cx="6" cy="6" r="5" fill="none" stroke="#fff" stroke-width="1.2"/><path d="M1 6h10M6 1c-2.5 3-2.5 7 0 10M6 1c2.5 3 2.5 7 0 10" fill="none" stroke="#fff" stroke-width="1"/></svg>
          www.corvaneinsulation.com
        </span>
      </div>
      <div class="contact-panel__address">87 Tilbury Road Marlow Creek, QLD, 4110</div>
    </div>
  </section>

  <section class="card card--back" aria-label="Business card back, white">
    <div class="wordmark"><span class="wordmark__square"></span>Corvane Insulation</div>
    <div class="website">www.corvaneinsulation.com</div>
  </section>

  <section class="card card--pattern" aria-label="Business card back, white alternative">
    <div class="wordmark">Corvane Insulation</div>
    <div class="website">www.corvaneinsulation.com</div>
  </section>

  <section class="card card--orange" aria-label="Business card back, orange">
    <div class="wordmark">Corvane Insulation</div>
    <div class="website">www.corvaneinsulation.com</div>
  </section>

</body>
</html>
```